Animal Eye Clinic needs a Business card

We are a new veterinary ophthalmology practice (Tessaly Animal Eye Care) and we need a business card designed. We only see animal eyes - we are not a regular veterinary clinic. We already have a logo. We are looking for a professional, good looking business card to hand out to our clients. We are looking for something simple but professional and contemporary. Our logo is likely the only picture/graphic that needs to be on the card.
Updates

Contact Information for Business Card

Marisol Dunkley, BSc, DVM, MSc, DipACVO
Veterinary Ophthalmologist

Phone: 250.418.3097
Email: tessalyanimaleyecare@mailbrook.net
Website: tessalyanimaleyecare.net
Address: 1840 Pellworth Rd
Kelowna, BC, V4T 8M3

Colors

Designer to choose colors to be used in the design.

Requirements
Must have
• Our logo (attached)

```html
<!DOCTYPE html>
<html lang="en">
<head>
<meta charset="utf-8">
<title>Tessaly Animal Eye Care – Business Card</title>
<link href="https://fonts.googleapis.com/css2?family=Roboto:wght@400;500;700&display=swap" rel="stylesheet">
<style>
  :root {
    --teal: #0a8c9c;
    --teal-light: #1fa3b2;
    --slate: #5a5b5d;
    --slate-dark: #4d4e50;
    --paper: #ffffff;
    --ink: #4a4a4a;
    --backdrop: #e9e7e4;
  }
  * { margin: 0; padding: 0; box-sizing: border-box; }
  html, body { width: 1200px; height: 847px; overflow: hidden; }
  body {
    background: var(--backdrop);
    font-family: "Roboto", Arial, sans-serif;
    position: relative;
  }
  .card {
    position: absolute;
    top: 270px;
    width: 520px;
    height: 297px;
    overflow: hidden;
    box-shadow: 0 6px 18px rgba(0,0,0,0.18);
  }
  .card--front { left: 50px; background: var(--slate); border-bottom: 5px solid var(--teal); }
  .card--back { left: 630px; background: var(--paper); border-bottom: 5px solid var(--teal); }

  .brand {
    display: flex;
    align-items: center;
    gap: 10px;
    color: var(--teal);
    font-weight: 500;
    letter-spacing: 0.5px;
  }
  .brand__dot {
    width: 30px; height: 30px; border-radius: 50%;
    background: var(--teal); flex-shrink: 0;
  }
  .card--front .brand {
    position: absolute; left: 50%; top: 50%;
    transform: translate(-50%, -50%);
    font-size: 28px; white-space: nowrap;
  }
  .card--front .brand__dot { width: 40px; height: 40px; }

  .card--back .brand {
    position: absolute; left: 28px; top: 26px; font-size: 19px;
  }
  .pointer {
    position: absolute; left: 0; top: 78px;
    width: 0; height: 0;
    border-top: 9px solid transparent;
    border-bottom: 9px solid transparent;
    border-left: 12px solid var(--teal);
  }
  .contact { position: absolute; left: 28px; top: 76px; color: var(--ink); }
  .contact__name {
    color: var(--teal); font-weight: 700; font-size: 19px; letter-spacing: 1.5px;
    text-transform: uppercase;
  }
  .contact__creds { color: var(--teal); font-size: 13px; margin-top: 3px; }
  .contact__title { font-size: 13px; margin-top: 2px; }
  .contact__address { font-size: 13px; line-height: 1.35; margin-top: 16px; }
  .contact__list { list-style: none; margin-top: 10px; font-size: 13px; line-height: 1.45; }
  .contact__list li { display: flex; align-items: center; gap: 5px; }
  .contact__list svg { width: 11px; height: 11px; fill: var(--teal); flex-shrink: 0; }

  .artwork {
    position: absolute; right: 0; bottom: 0;
    width: 210px; height: 230px;
    border-top-left-radius: 120px;
    background: linear-gradient(160deg, var(--teal-light) 0%, var(--teal) 60%, var(--slate-dark) 100%);
  }
</style>
</head>
<body>
  <section class="card card--front" aria-label="Business card front">
    <div class="brand"><span class="brand__dot"></span>Tessaly Animal Eye Care</div>
  </section>

  <section class="card card--back" aria-label="Business card back">
    <div class="brand"><span class="brand__dot"></span>Tessaly Animal Eye Care</div>
    <span class="pointer"></span>
    <div class="contact">
      <p class="contact__name">Marisol Dunkley</p>
      <p class="contact__creds">BSc, DVM, MSc, DipACVO</p>
      <p class="contact__title">Veterinary Ophthalmologist</p>
      <p class="contact__address">1840 Pellworth Rd<br>Kelowna, BC, V4T 8M3</p>
      <ul class="contact__list">
        <li><svg viewBox="0 0 24 24"><path d="M6.6 10.8a15 15 0 0 0 6.6 6.6l2.2-2.2c.3-.3.7-.4 1-.2 1.1.4 2.3.6 3.6.6.6 0 1 .4 1 1V20c0 .6-.4 1-1 1A17 17 0 0 1 3 4c0-.6.4-1 1-1h3.5c.6 0 1 .4 1 1 0 1.3.2 2.5.6 3.6.1.3 0 .7-.2 1z"/></svg>250.418.3097</li>
        <li><svg viewBox="0 0 24 24"><path d="M2 5h20v14H2zm2 2v.4l8 5 8-5V7l-8 5z"/></svg>tessalyanimaleyecare@mailbrook.net</li>
        <li><svg viewBox="0 0 24 24"><path d="M12 2a10 10 0 1 0 0 20 10 10 0 0 0 0-20zm6.9 9h-3a15 15 0 0 0-1.3-5.6A8 8 0 0 1 18.9 11zM12 4c.9 1.2 1.7 3.6 1.9 7h-3.8c.2-3.4 1-5.8 1.9-7zM9.4 5.4A15 15 0 0 0 8.1 11h-3a8 8 0 0 1 4.3-5.6zM5.1 13h3a15 15 0 0 0 1.3 5.6A8 8 0 0 1 5.1 13zm6.9 7c-.9-1.2-1.7-3.6-1.9-7h3.8c-.2 3.4-1 5.8-1.9 7zm2.6-1.4a15 15 0 0 0 1.3-5.6h3a8 8 0 0 1-4.3 5.6z"/></svg>tessalyanimaleyecare.net</li>
      </ul>
    </div>
    <div class="artwork" role="img" aria-label="Illustration of a horse, cat and dog in profile silhouette"></div>
  </section>
</body>
</html>
```